Visitenkarten
Zielgruppe
Wir handeln und restaurieren (mit) sehr hochwertigen Fahrzeugen (Oldtimier/Supercars) bis in den Bereich von mehreren Millionen Euro. Die Zielgruppe sind potentielle Käufer im sehr gehobenen Premium Segment.
Aufgabenstellung
Eine Visitenkarte im Idealfall mit dem schwarzen Logo soll erstellt werden. Standardformat oder ein kreatives, aber praktikables Format. Ziel ist eine sehr hochwertige, geprägte Visitenkarte. Frontseite das Velvet Marques Logo, Rückseite einmal: Jonas Wehrberg, Owner, Phone +436601742863, Email Sales@velvet-marques.com Salzburg Dobrovnik (generisch anpassbare Adresse)

```html
<!DOCTYPE html>
<html lang="de">
<head>
<meta charset="utf-8">
<title>Velvet Marques – Visitenkarten</title>
<link rel="stylesheet" href="https://fonts.googleapis.com/css2?family=Jost:wght@300;400&display=swap">
<style>
  :root {
    --stage-light: #ffffff;
    --stage-mid: #7b7780;
    --stage-dark: #000000;
    --card-black: #07070c;
    --card-graphite: #26272c;
    --gold-light: #efcfa0;
    --gold-mid: #c99c6c;
    --gold-deep: #8a6240;
    --bronze-dark: #4a3320;
    --ink-white: #ffffff;
  }
  * { margin: 0; padding: 0; box-sizing: border-box; }
  html, body { width: 1200px; height: 675px; overflow: hidden; }
  body {
    position: relative;
    background: linear-gradient(150deg, var(--stage-light) 0%, var(--stage-mid) 40%, #45434a 70%, var(--stage-dark) 100%);
    font-family: "Jost", sans-serif;
    color: var(--ink-white);
  }
  .card {
    position: absolute;
    top: 200px;
    width: 419px;
    height: 276px;
    display: flex;
    box-shadow: 3px 4px 5px rgba(0,0,0,0.35);
  }
  .card--front { left: 146px; }
  .card--back { left: 636px; }

  .gold-pattern {
    width: 75px;
    height: 100%;
    background: linear-gradient(100deg, var(--gold-mid) 0%, var(--gold-light) 30%, var(--gold-mid) 60%, var(--gold-light) 85%, var(--gold-mid) 100%);
  }
  .bronze-band {
    width: 9px;
    height: 100%;
    background: linear-gradient(180deg, var(--gold-deep) 0%, var(--bronze-dark) 50%, var(--gold-light) 85%, var(--gold-deep) 100%);
  }
  .card__panel {
    flex: 1;
    position: relative;
    height: 100%;
  }
  .card--front .card__panel {
    background: linear-gradient(90deg, var(--card-graphite) 0%, #0d0e16 40%, #020204 55%, #0d0e16 70%, var(--card-graphite) 100%);
  }
  .card--back .card__panel {
    background: linear-gradient(180deg, var(--card-graphite) 0%, #0b0c14 40%, #050509 55%, #16171c 80%, var(--card-graphite) 100%);
  }

  .brand-name {
    position: absolute;
    left: 0; right: 0;
    top: 120px;
    text-align: center;
    font-family: "Jost", sans-serif;
    font-weight: 400;
    font-size: 28px;
    letter-spacing: 2px;
    color: var(--ink-white);
    white-space: nowrap;
  }

  .contact {
    position: absolute;
    left: 0; right: 0;
    text-align: center;
    white-space: nowrap;
  }
  .contact__name { top: 108px; font-size: 18px; font-weight: 400; letter-spacing: 2px; }
  .contact__role { top: 134px; font-size: 14px; font-weight: 300; letter-spacing: 1.2px; }
  .contact__city { top: 172px; font-size: 12.5px; font-weight: 400; letter-spacing: 1px; }
  .contact__email { top: 198px; font-size: 12.5px; font-weight: 400; letter-spacing: 1px; }
  .contact__phone { top: 224px; font-size: 12.5px; font-weight: 400; letter-spacing: 1.4px; }
</style>
</head>
<body>
  <section class="card card--front">
    <div class="gold-pattern" role="img" aria-label="Goldenes geometrisches Rautenmuster"></div>
    <div class="bronze-band"></div>
    <div class="card__panel">
      <p class="brand-name">Velvet Marques</p>
    </div>
    <div class="bronze-band"></div>
    <div class="gold-pattern" role="img" aria-label="Goldenes geometrisches Rautenmuster"></div>
  </section>

  <section class="card card--back">
    <div class="gold-pattern" role="img" aria-label="Goldenes geometrisches Rautenmuster"></div>
    <div class="bronze-band"></div>
    <div class="card__panel">
      <p class="contact contact__name">Jonas Wehrberg</p>
      <p class="contact contact__role">Owner</p>
      <p class="contact contact__city">Kellheim / Varosina</p>
      <p class="contact contact__email">sales@velvet-marques.com</p>
      <p class="contact contact__phone">+43 66 01 74 28 63</p>
    </div>
    <div class="bronze-band"></div>
    <div class="gold-pattern" role="img" aria-label="Goldenes geometrisches Rautenmuster"></div>
  </section>
</body>
</html>
```